Brivane - Business Cards for a new venture

create business card for a startup classified business dealing in construction materials, the cards need to have a professional look but modern, more serious than playful, one of the samples must include the official font (attached), please explore using the official colors in the company's logo

Target Market(s)

Energy sector

Contact Information for Business Card

Font styles to use
Other font styles liked:
• suissnord

Requirements
Must have
• corporate colors (in logo attached)
Nice to have
• Official font (in one of the samples) font is : suissnord
Should not have
• Cartoonish look

```html
<!DOCTYPE html>
<html lang="en">
<head>
<meta charset="utf-8">
<title>Brivane Business Cards</title>
<link rel="stylesheet" href="https://fonts.googleapis.com/css2?family=Exo+2:wght@400;600;700&display=swap">
<style>
  :root {
    --backdrop: #2b2b2d;
    --navy: #123f78;
    --navy-deep: #0d2f5e;
    --navy-light: #1c4f8f;
    --card-white: #f4f4f4;
    --ink: #1a1a1a;
    --grey: #8c8c8c;
    --white: #ffffff;
  }
  * { margin: 0; padding: 0; box-sizing: border-box; }
  html, body {
    width: 1200px;
    height: 997px;
    overflow: hidden;
    background: var(--backdrop);
    font-family: "Exo 2", sans-serif;
  }
  .stage {
    position: relative;
    width: 1200px;
    height: 997px;
  }
  .card {
    position: absolute;
    left: 300px;
    width: 600px;
    height: 343px;
    overflow: hidden;
    box-shadow: 0 16px 40px rgba(0,0,0,0.45);
  }

  /* Front card */
  .card-front { top: 125px; }
  .front-surface {
    position: absolute;
    inset: 0;
    background: linear-gradient(135deg, var(--navy-light) 0%, var(--navy) 45%, var(--navy-deep) 100%);
  }
  .front-brand {
    position: absolute;
    left: 0; right: 0;
    top: 128px;
    text-align: center;
    color: var(--white);
    font-weight: 600;
    font-size: 54px;
    letter-spacing: 10px;
    text-transform: uppercase;
  }
  .front-url {
    position: absolute;
    left: 0; right: 0;
    top: 232px;
    text-align: center;
    color: rgba(255,255,255,0.8);
    font-weight: 400;
    font-size: 12px;
    letter-spacing: 6px;
  }

  /* Back card */
  .card-back {
    top: 528px;
    background: var(--card-white);
  }
  .back-brand {
    position: absolute;
    left: 0; right: 0;
    top: 58px;
    display: flex;
    justify-content: center;
    align-items: center;
    gap: 14px;
    color: var(--navy);
    font-weight: 600;
    font-size: 34px;
    letter-spacing: 8px;
    text-transform: uppercase;
  }
  .brand-dot {
    width: 14px;
    height: 14px;
    border-radius: 50%;
    background: var(--grey);
  }
  .holder {
    position: absolute;
    right: 318px;
    top: 178px;
    text-align: right;
    color: var(--navy);
  }
  .holder-name { font-weight: 700; font-size: 19px; line-height: 1.1; }
  .holder-firm { font-weight: 400; font-size: 11px; color: var(--ink); margin-bottom: 16px; }
  .holder-address { font-weight: 700; font-size: 17px; line-height: 1.2; }
  .divider {
    position: absolute;
    left: 298px;
    top: 168px;
    width: 2px;
    height: 96px;
    background: linear-gradient(to bottom, rgba(18,63,120,0), var(--navy) 30%, rgba(18,63,120,0));
  }
  .contacts {
    position: absolute;
    left: 318px;
    top: 166px;
    list-style: none;
  }
  .contact {
    display: flex;
    align-items: center;
    gap: 10px;
    height: 30px;
    font-size: 14px;
    color: var(--ink);
  }
  .contact-icon {
    width: 20px;
    height: 20px;
    border-radius: 50%;
    background: var(--navy);
    display: flex;
    align-items: center;
    justify-content: center;
  }
  .back-band {
    position: absolute;
    left: 0; right: 0; bottom: 0;
    height: 20px;
    background: var(--navy);
  }
</style>
</head>
<body>
<main class="stage">

  <section class="card card-front">
    <div class="front-surface" role="img" aria-label="Deep blue faceted polygon texture"></div>
    <div class="front-brand">Brivane</div>
    <div class="front-url">www.brivane.com</div>
  </section>

  <section class="card card-back">
    <div class="back-brand"><span class="brand-dot"></span>Brivane</div>

    <div class="holder">
      <div class="holder-name">Helena Marwick</div>
      <div class="holder-firm">KVRL Partners</div>
      <div class="holder-address">41-17 58th St<br>Ridgeport NY 11482</div>
    </div>

    <div class="divider"></div>

    <ul class="contacts">
      <li class="contact">
        <span class="contact-icon">
          <svg width="12" height="12" viewBox="0 0 24 24"><path fill="#fff" d="M6.6 10.8a15 15 0 0 0 6.6 6.6l2.2-2.2a1 1 0 0 1 1-.25 11.4 11.4 0 0 0 3.6.57 1 1 0 0 1 1 1V20a1 1 0 0 1-1 1A17 17 0 0 1 3 4a1 1 0 0 1 1-1h3.5a1 1 0 0 1 1 1c0 1.25.2 2.45.57 3.57a1 1 0 0 1-.25 1z"/></svg>
        </span>
        (555) 210-4873
      </li>
      <li class="contact">
        <span class="contact-icon">
          <svg width="12" height="12" viewBox="0 0 24 24"><rect x="7" y="2" width="10" height="20" rx="2" fill="none" stroke="#fff" stroke-width="2"/><circle cx="12" cy="18" r="1.2" fill="#fff"/></svg>
        </span>
        (555) 384-1962
      </li>
      <li class="contact">
        <span class="contact-icon">
          <svg width="12" height="12" viewBox="0 0 24 24"><rect x="3" y="6" width="18" height="12" rx="1" fill="none" stroke="#fff" stroke-width="2"/><path d="M3 7l9 6 9-6" fill="none" stroke="#fff" stroke-width="2"/></svg>
        </span>
        hmarwick@brivane.com
      </li>
    </ul>

    <div class="back-band"></div>
  </section>

</main>
</body>
</html>
```